Eye-Catching, Direct Marketing Residential Painting Flyer!

I am run a residential painting business and am looking for a flyer to be designed to mailout to potential customers.
I want the copy/wording to be designed similar to this flyer.

It's important that the person reading the flyer gets the benefits we're promoting which is why I want the wording/copy to be almost identical to the flyer attached.

However, the structure will be different. The flyer will be a postcard thick, 5 x11.5.
Double sided.

The name of the company is Brightwall Coaters.

I would also like the prominent colour to either be light green or orange.

Target Market(s)

Home Owners between the age of 45-80.

Industry/Entity Type

Painting And Decorating

Font styles to use
Serif

Colors
f68d4d
faa54b
f78f20
f37122
9bcb3c
abd037
cadf82

Requirements
Must have
• Excellent Eye-Catching Design
• Benefits Visibly Promoted
• Action Taking Incentive- Call Now for FREE Window Cleaning and FREE Painting Estimate
Should not have
• Crowded wording

```html
<!DOCTYPE html>
<html lang="en">
<head>
<meta charset="utf-8">
<title>Brightwall Coaters – Flyer</title>
<link rel="stylesheet" href="https://fonts.googleapis.com/css2?family=Oswald:wght@400;500;600;700&family=Roboto+Condensed:wght@400;700&display=swap">
<style>
  :root {
    --green: #9bcb3c;
    --green-mid: #abd037;
    --green-light: #cadf82;
    --green-deep: #4caf2a;
    --ink: #111111;
    --white: #ffffff;
    --canvas: #f1f1ef;
  }
  * { box-sizing: border-box; margin: 0; padding: 0; }
  html, body { width: 1200px; height: 1200px; overflow: hidden; background: var(--canvas); }
  body { position: relative; font-family: "Oswald", "Arial Narrow", sans-serif; color: var(--ink); }

  .flyer {
    position: absolute; top: 108px; width: 428px; height: 984px;
    background: var(--white); overflow: hidden;
    box-shadow: 0 2px 8px rgba(0,0,0,.12);
  }
  .flyer--front { left: 126px; }
  .flyer--back { left: 646px; }
  .abs { position: absolute; }

  /* front top band */
  .top-band { left: 0; top: 0; width: 428px; height: 78px; background: var(--green); }
  .top-band__title {
    left: 0; width: 428px; top: 12px; text-align: center; color: var(--white);
    font-weight: 500; font-size: 26px; line-height: 27px; letter-spacing: .3px;
  }
  .top-band__mark { top: 22px; width: 34px; height: 34px; background: var(--green-light); border-radius: 3px; }

  .headline {
    left: 10px; width: 408px; top: 118px; text-align: center;
    font-weight: 600; font-size: 31px; line-height: 39px; text-transform: uppercase; letter-spacing: -.2px;
  }
  .hl-light { color: var(--green); }
  .hl-deep { color: var(--green-deep); }

  /* brand band */
  .brand-band { left: 0; top: 428px; width: 428px; height: 42px; background: var(--green); }
  .brand-band__inner { left: 0; top: 434px; width: 360px; height: 30px; background: var(--white); }
  .brand-name { font-weight: 600; color: var(--ink); white-space: nowrap; }
  .brand-band__label { left: 30px; top: 434px; font-size: 30px; line-height: 30px; }
  .brand-dot {
    width: 84px; height: 84px; border-radius: 50%;
    background: var(--white); border: 7px solid var(--green);
  }
  .flyer--front .brand-dot { left: 341px; top: 408px; }

  .team-photo {
    left: -40px; top: 384px; width: 300px; height: 300px; border-radius: 50%;
    border: 5px solid var(--green);
    background: radial-gradient(circle at 55% 60%, #d9dcd8 0%, #a6aba4 45%, #5f7a48 100%);
  }
  .promise {
    left: 280px; width: 132px; top: 496px; text-align: center;
    font-weight: 600; line-height: 24px; text-transform: uppercase;
  }
  .promise__lead { font-size: 23px; color: var(--ink); }
  .promise__big { font-size: 29px; line-height: 27px; color: var(--green); margin-top: 2px; }

  /* call now */
  .divider { left: 0; width: 428px; height: 12px; background: var(--green-light); }
  .divider__notch { width: 0; height: 0; border-left: 20px solid transparent; border-right: 20px solid transparent; border-top: 16px solid var(--green-light); }
  .call-now { left: 0; width: 428px; text-align: center; color: var(--green); font-weight: 500; font-size: 52px; line-height: 52px; letter-spacing: .5px; }
  .offer { left: 0; width: 428px; text-align: center; font-weight: 500; font-size: 25px; line-height: 28px; text-transform: uppercase; }

  .contact-band { left: 0; width: 428px; height: 140px; background: var(--green); }
  .contact { left: 14px; color: var(--white); }
  .contact__phone { display: flex; align-items: center; gap: 6px; font-weight: 500; font-size: 38px; line-height: 44px; }
  .contact__web { font-family: "Roboto Condensed", sans-serif; font-size: 27px; line-height: 32px; }
  .contact__social { display: flex; align-items: center; gap: 8px; font-family: "Roboto Condensed", sans-serif; font-size: 16px; line-height: 22px; }
  .contact__square { width: 16px; height: 16px; background: var(--white); }
  .mascot {
    width: 150px; height: 150px; border-radius: 50%; border: 5px solid var(--white);
    background: linear-gradient(160deg, #dbe9f4 0%, #9fc3e0 55%, #b33a2a 100%);
  }

  /* back */
  .back-band { left: 56px; top: 34px; width: 372px; height: 40px; background: var(--green); }
  .flyer--back .brand-name { left: 118px; top: 28px; font-size: 33px; line-height: 52px; }
  .flyer--back .brand-dot { left: 18px; top: 14px; width: 78px; height: 78px; }

  .pair-label { font-weight: 600; color: var(--green); font-size: 16px; line-height: 18px; text-transform: uppercase; }
  .pair-copy { font-family: "Roboto Condensed", sans-serif; font-size: 11px; line-height: 13px; color: var(--ink); }
  .pair-block { width: 140px; }
  .pair-block--right { text-align: right; }
  .pair-icon { width: 12px; height: 30px; border-radius: 4px 4px 2px 2px; background: var(--green-light); }
  .pair-icon--solid { background: var(--green); }

  .shot { width: 118px; height: 118px; border-radius: 50%; border: 4px solid var(--green-light); }
  .shot--after { border-color: var(--green); }
  .chevron { width: 0; height: 0; border-top: 14px solid transparent; border-bottom: 14px solid transparent; border-left: 14px solid var(--green-light); }
</style>
</head>
<body>

<!-- FRONT -->
<section class="flyer flyer--front">
  <div class="abs top-band"></div>
  <div class="abs top-band__mark" style="left:32px"></div>
  <div class="abs top-band__mark" style="left:362px"></div>
  <h2 class="abs top-band__title">TAKE CONTROL OF HOW<br>YOUR HOME LOOKS!</h2>

  <h1 class="abs headline">
    Do your <span class="hl-light">deck</span>, <span class="hl-light">interior</span>,<br>
    <span class="hl-light">siding walls</span>, <span class="hl-light">fence</span>,<br>
    <span class="hl-light">windows</span> look <span class="hl-deep">faded</span>,<br>
    <span class="hl-deep">dirty</span>, <span class="hl-deep">out of date</span>, are<br>
    they <span class="hl-deep">chipping</span> or <span class="hl-deep">peeling</span>?<br>
    Has the <span class="hl-light">wood</span> started<br>
    to <span class="hl-deep">rot</span> yet?
  </h1>

  <div class="abs team-photo" role="img" aria-label="Photo of the three-person painting crew in paint-spattered shirts"></div>

  <div class="abs brand-band"></div>
  <div class="abs brand-band__inner"></div>
  <span class="abs brand-name brand-band__label">BRIGHTWALL COATERS</span>
  <div class="abs brand-dot"></div>

  <div class="abs promise">
    <div class="promise__lead">We<br>make your<br>home look</div>
    <div class="promise__big">Clean,<br>fresh &amp;<br>beautiful<br>again!</div>
  </div>

  <div class="abs divider" style="top:700px"></div>
  <div class="abs divider__notch" style="left:194px;top:712px"></div>
  <div class="abs call-now" style="top:730px">CALL NOW</div>
  <div class="abs offer" style="top:782px">For free window cleaning<br>&amp; free painting estimate</div>

  <div class="abs contact-band" style="top:852px"></div>
  <div class="abs contact" style="top:860px">
    <div class="contact__phone">
      <svg width="24" height="34" viewBox="0 0 24 34" aria-hidden="true"><path d="M7 2 L12 9 L8 13 Q9 21 14 25 L18 21 L23 27 L18 32 Q3 28 2 8 Z" fill="#fff"/></svg>
      555-014-2290
    </div>
    <div class="contact__web">brightwallcoaters.com</div>
    <div class="contact__social"><span class="contact__square"></span>social: @brightwallcoaters</div>
  </div>
  <div class="abs mascot" style="left:300px;top:840px" role="img" aria-label="Illustration of a painter in a blue cap holding a paintbrush"></div>
</section>

<!-- BACK -->
<section class="flyer flyer--back">
  <div class="abs back-band"></div>
  <div class="abs brand-dot"></div>
  <span class="abs brand-name">BRIGHTWALL COATERS</span>

  <!-- row 1 -->
  <div class="abs pair-icon" style="left:24px;top:118px"></div>
  <div class="abs pair-icon pair-icon--solid" style="left:24px;top:186px"></div>
  <div class="abs pair-block" style="left:46px;top:118px">
    <div class="pair-label">Problem</div>
    <div class="pair-copy">Your deck or fence is chipping or peeling, and looks old and faded.</div>
    <div class="pair-label" style="margin-top:12px">Solution</div>
    <div class="pair-copy">A fresh coat of stain will protect your investment and make it look clean, fresh and beautiful again!</div>
  </div>
  <div class="abs shot" style="left:182px;top:124px;background:linear-gradient(150deg,#b8b2a4,#d9c79a 50%,#8f8a80)" role="img" aria-label="Before: worn, peeling wooden deck steps"></div>
  <div class="abs shot shot--after" style="left:298px;top:124px;background:linear-gradient(150deg,#b9bcbd,#6d7173 60%,#5a5e60)" role="img" aria-label="After: freshly stained grey deck steps"></div>
  <div class="abs chevron" style="left:296px;top:168px"></div>

  <!-- row 2 -->
  <div class="abs shot" style="left:14px;top:292px;background:linear-gradient(160deg,#e6e8ea,#8a4a38 55%,#4c5a3a)" role="img" aria-label="Before: brick house with faded trim"></div>
  <div class="abs shot shot--after" style="left:132px;top:292px;background:linear-gradient(160deg,#eef0f2,#9a5440 55%,#4f6a3c)" role="img" aria-label="After: brick house with freshly painted trim"></div>
  <div class="abs chevron" style="left:130px;top:336px"></div>
  <div class="abs pair-block pair-block--right" style="left:244px;top:276px">
    <div class="pair-label">Problem</div>
    <div class="pair-copy">Your exterior windows, doors, garage doors, stucco, siding, soffits are chipping or peeling, and look old and faded.</div>
    <div class="pair-label" style="margin-top:12px">Solution</div>
    <div class="pair-copy">A fresh coat of stain will protect your investment and make it look clean, fresh and beautiful again!</div>
  </div>
  <div class="abs pair-icon" style="left:394px;top:276px"></div>
  <div class="abs pair-icon pair-icon--solid" style="left:394px;top:356px"></div>

  <!-- row 3 -->
  <div class="abs pair-icon" style="left:22px;top:444px"></div>
  <div class="abs pair-icon pair-icon--solid" style="left:22px;top:536px"></div>
  <div class="abs pair-block" style="left:44px;top:442px">
    <div class="pair-label">Problem</div>
    <div class="pair-copy">Is the colour in your interior basement, kitchen, bedrooms and bathrooms walls, doors, and trim faded or out-of-date?</div>
    <div class="pair-label" style="margin-top:12px">Solution</div>
    <div class="pair-copy">A fresh coat of paint to make your interior look clean, fresh and beautiful again!</div>
  </div>
  <div class="abs shot" style="left:180px;top:452px;background:linear-gradient(150deg,#a9774e,#c79a70 55%,#e6e1da)" role="img" aria-label="Before: dated tan interior wall"></div>
  <div class="abs shot shot--after" style="left:294px;top:452px;background:linear-gradient(150deg,#d5d6d8,#eeeff0 60%,#cfd1d3)" role="img" aria-label="After: freshly painted light grey interior wall"></div>
  <div class="abs chevron" style="left:292px;top:496px"></div>

  <!-- row 4 -->
  <div class="abs shot" style="left:14px;top:614px;background:linear-gradient(165deg,#c9a77e,#8f7454 55%,#d0b895)" role="img" aria-label="Before: weathered wooden deck boards"></div>
  <div class="abs shot shot--after" style="left:132px;top:614px;background:linear-gradient(165deg,#a0523a,#7a3522 55%,#b56a4a)" role="img" aria-label="After: deck boards with fresh red-brown stain"></div>
  <div class="abs chevron" style="left:130px;top:658px"></div>
  <div class="abs pair-block pair-block--right" style="left:244px;top:614px">
    <div class="pair-label">Problem</div>
    <div class="pair-copy">Your exterior semi-transparent deck, fence or siding is peeling, chipping or faded.</div>
    <div class="pair-label" style="margin-top:12px">Solution</div>
    <div class="pair-copy">A fresh coat of stain to protect the wood and make it look clean, fresh and beautiful!</div>
  </div>
  <div class="abs pair-icon" style="left:394px;top:612px"></div>
  <div class="abs pair-icon pair-icon--solid" style="left:394px;top:684px"></div>

  <div class="abs divider" style="top:760px;height:16px"></div>
  <div class="abs divider__notch" style="left:194px;top:776px"></div>
  <div class="abs call-now" style="top:800px">CALL NOW</div>

  <div class="abs contact-band" style="top:856px;height:128px"></div>
  <div class="abs contact" style="top:864px">
    <div class="contact__phone">
      <svg width="24" height="34" viewBox="0 0 24 34" aria-hidden="true"><path d="M7 2 L12 9 L8 13 Q9 21 14 25 L18 21 L23 27 L18 32 Q3 28 2 8 Z" fill="#fff"/></svg>
      555-014-2290
    </div>
    <div class="contact__web">brightwallcoaters.com</div>
    <div class="contact__social"><span class="contact__square"></span>social: @brightwallcoaters</div>
  </div>
  <div class="abs mascot" style="left:290px;top:838px" role="img" aria-label="Illustration of a painter in a blue cap holding a paintbrush"></div>
</section>

</body>
</html>
```